Cash Flow Slide Design

Help Make Slide flow, QB Lantern to paying Down HELOC Then Bring in new Home Purchase and look amazing.
Font styles to use
Serif
Colors
EB3D1F
EC4F4E
F09395
F8D3D4
FCEDEE

```html
<!DOCTYPE html>
<html lang="en">
<head>
<meta charset="utf-8">
<title>Wealth Builder Account – Offset Account</title>
<link rel="stylesheet" href="https://fonts.googleapis.com/css2?family=Lora:wght@600;700&display=swap">
<style>
  :root {
    --red: #eb3d1f;
    --coral: #ec4f4e;
    --rose: #f09395;
    --blush: #f8d3d4;
    --mist: #fcedee;
    --rose-deep: #b3333f;
    --wine: #7e2430;
    --ember: #c42f18;
    --ink: #3a1f1f;
    --white: #ffffff;
  }
  html, body {
    margin: 0;
    padding: 0;
    width: 1200px;
    height: 679px;
    overflow: hidden;
    background: var(--mist);
    font-family: "Lora", serif;
  }
  .canvas { position: relative; width: 1200px; height: 679px; }
  .slide {
    position: absolute; left: 100px; top: 56px;
    width: 1000px; height: 562px; background: var(--white);
  }
  .title-band {
    position: absolute; left: 100px; top: 73px;
    width: 439px; height: 56px;
    background: var(--red);
    border-radius: 0 28px 28px 0;
  }
  .title-band h1 {
    margin: 0; padding-left: 18px;
    font-size: 30px; line-height: 56px; font-weight: 700;
    color: var(--white);
  }
  .brand {
    position: absolute; left: 862px; top: 84px;
    display: flex; align-items: center; gap: 8px;
  }
  .brand-dot { width: 26px; height: 26px; border-radius: 50%; background: var(--red); }
  .brand-name { font-size: 26px; font-weight: 700; color: var(--ink); line-height: 34px; }
  .subtitle {
    position: absolute; left: 0; width: 1200px; top: 145px;
    margin: 0; text-align: center;
    font-size: 28px; font-weight: 700; color: var(--ink);
  }
  .subtitle .accent { color: var(--coral); }
  .diagram { position: absolute; left: 0; top: 0; }
  .label { font-family: "Lora", serif; font-weight: 700; }
  .slide-number {
    position: absolute; left: 1113px; top: 610px;
    font-size: 8px; font-weight: 700; color: var(--ink);
  }
</style>
</head>
<body>
<div class="canvas">
  <div class="slide"></div>

  <div class="title-band"><h1>Wealth Builder Account</h1></div>

  <div class="brand">
    <span class="brand-dot"></span>
    <span class="brand-name">Northmark</span>
  </div>

  <h2 class="subtitle">Offset Account: <span class="accent">Permanent Life Insurance</span></h2>

  <svg class="diagram" width="1200" height="679" viewBox="0 0 1200 679">
    <defs>
      <clipPath id="col-checking"><rect x="239" y="223" width="132" height="329" rx="9"/></clipPath>
      <clipPath id="col-oa"><rect x="480" y="224" width="132" height="328" rx="9"/></clipPath>
      <clipPath id="col-heloc"><rect x="714" y="223" width="132" height="329" rx="9"/></clipPath>
    </defs>

    <!-- Checking column -->
    <g class="column column-checking" clip-path="url(#col-checking)">
      <rect x="239" y="223" width="132" height="329" fill="var(--blush)"/>
      <rect x="239" y="381" width="132" height="171" fill="var(--rose)"/>
      <polygon points="239,223 371,223 371,258 305,284 239,258" fill="var(--coral)"/>
    </g>
    <text class="label" x="305" y="254" text-anchor="middle" font-size="17" fill="var(--white)">Checking</text>

    <!-- OA life insurance column -->
    <g class="column column-oa" clip-path="url(#col-oa)">
      <rect x="480" y="224" width="132" height="328" fill="var(--blush)"/>
      <rect x="480" y="363" width="132" height="189" fill="var(--coral)"/>
      <polygon points="535,363 557,363 546,375" fill="var(--blush)"/>
      <polygon points="480,224 612,224 612,272 546,300 480,272" fill="var(--red)"/>
    </g>
    <text class="label" text-anchor="middle" font-size="16" fill="var(--white)">
      <tspan x="546" y="251">OA Life</tspan><tspan x="546" y="271">Insurance</tspan>
    </text>
    <text class="label" text-anchor="middle" font-size="14" fill="var(--ink)">
      <tspan x="546" y="329">Optimal</tspan><tspan x="546" y="349">Transfer Point</tspan>
    </text>

    <g class="benefits" fill="none" stroke="var(--white)" stroke-width="1.3" stroke-linecap="round" stroke-linejoin="round">
      <circle cx="545" cy="392" r="6.5"/><path d="M542 392 l2.2 2.2 l4 -4"/>
      <circle cx="545" cy="464" r="6.5"/><path d="M542 464 l2.2 2.2 l4 -4"/>
      <circle cx="545" cy="519" r="6.5"/><path d="M542 519 l2.2 2.2 l4 -4"/>
    </g>
    <text class="label" text-anchor="middle" font-size="11.5" fill="var(--white)">
      <tspan x="546" y="416">Cash Value</tspan>
      <tspan x="546" y="430.5">continues to</tspan>
      <tspan x="546" y="445">grow</tspan>
      <tspan x="546" y="485">Can never lose</tspan>
      <tspan x="546" y="500">Principal</tspan>
      <tspan x="546" y="541">Cash Value</tspan>
    </text>

    <!-- HELOC column -->
    <g class="column column-heloc" clip-path="url(#col-heloc)">
      <rect x="714" y="223" width="132" height="329" fill="var(--blush)"/>
      <rect x="714" y="485" width="132" height="67" fill="var(--rose)"/>
      <polygon points="714,223 846,223 846,258 780,284 714,258" fill="var(--ember)"/>
    </g>
    <text class="label" x="780" y="254" text-anchor="middle" font-size="16" fill="var(--white)">HELOC</text>

    <!-- New home column -->
    <rect class="column column-home" x="947" y="223" width="132" height="329" rx="9" fill="var(--blush)"/>
    <text class="label" text-anchor="middle" font-size="15.5" fill="var(--red)">
      <tspan x="1013" y="338">New Home</tspan><tspan x="1013" y="358">Purchase</tspan>
    </text>
    <rect class="home-illustration" role="img" aria-label="House illustration" x="981" y="388" width="65" height="65" rx="6" fill="var(--rose)"/>

    <!-- Income arrows -->
    <g class="flow flow-income" fill="var(--rose-deep)">
      <polygon points="114,381 175,381 175,358 229,402 175,447 175,424 114,424"/>
      <polygon points="114,481 175,481 175,458 229,502 175,547 175,524 114,524"/>
    </g>
    <g class="label" font-size="16" fill="var(--white)">
      <text x="124" y="408">$</text><text x="140" y="408">Income</text>
      <text x="124" y="508">$</text><text x="140" y="508">Income</text>
    </g>

    <!-- Funds transfer arrows -->
    <g class="flow flow-transfer" fill="var(--rose-deep)">
      <polygon points="371,381 432,381 432,358 487,402 432,447 432,424 371,424"/>
      <polygon points="371,481 432,481 432,458 487,502 432,547 432,524 371,524"/>
    </g>
    <g class="sync-icon" fill="none" stroke="var(--white)" stroke-width="1.8" stroke-linecap="round">
      <path d="M381 400 a6.5 6.5 0 0 1 11.5 -3.5 M393 397 v-4 M393 397 h-4"/>
      <path d="M394 404 a6.5 6.5 0 0 1 -11.5 3.5 M382 407 v4 M382 407 h4"/>
      <path d="M381 500 a6.5 6.5 0 0 1 11.5 -3.5 M393 497 v-4 M393 497 h-4"/>
      <path d="M394 504 a6.5 6.5 0 0 1 -11.5 3.5 M382 507 v4 M382 507 h4"/>
    </g>
    <g class="label" font-size="13.5" fill="var(--white)" text-anchor="middle">
      <text><tspan x="434" y="399">Funds</tspan><tspan x="434" y="415">Transfer</tspan></text>
      <text><tspan x="434" y="498">Funds</tspan><tspan x="434" y="514">Transfer</tspan></text>
    </g>

    <!-- QB Lantern arrow to HELOC -->
    <polygon class="flow flow-paydown" points="612,363 674,363 674,339 727,384 674,429 674,406 612,406" fill="var(--red)"/>
    <text class="label" text-anchor="middle" font-size="12" fill="var(--white)">
      <tspan x="654" y="381">QB</tspan><tspan x="654" y="395">Lantern</tspan>
    </text>

    <!-- New home purchase arrow -->
    <polygon class="flow flow-purchase" points="847,399 908,399 908,376 963,420 908,465 908,441 847,441" fill="var(--wine)"/>
    <text class="label" text-anchor="middle" font-size="13.5" fill="var(--white)">
      <tspan x="897" y="416">New Home</tspan><tspan x="895" y="431">Purchase</tspan>
    </text>
  </svg>

  <div class="slide-number">X10</div>
</div>
</body>
</html>
```